Professional Price List Design for Luxury Candle Range (Print-Ready)

This project requires a luxury, calm, high-end price list — not a flyer, not a basic price sheet. I am wanting mainly soft whites, warm creams, beige, subtle gold tones - no bold colours. Layout to be clearly sectioned by candle range; each range must read as a distinct feature, while flowing cohesively on one page (ideally without looking cramped).
Use clean margins and balanced spacing.
Overall layout should resemble a boutique catalogue or luxury menu
Use some of the supplied candle images only, true to size (no distortion)
Elegant, refined typography is essential

If this style or level of refinement is not aligned with your design approach, please do not submit an entry.

Target Market(s)

Individuals interested in wellness, mindfulness, and soulful living

Industry/Entity Type

Wellness & Lifestyle Brand

Colors

Designer to choose colors to be used in the design.

Requirements
Must have
• A design that allows for future updates as new products are released. Contact email clearly visible for ordering
Nice to have
• Some snap shots of each different candle ranges - I have attached individual photos to brief - they DO NOT all have to be included, they are just examples in case you want to use them.
Should not have
• No loud colours. No crowded pricing or tight spacing.

```html
<!DOCTYPE html>
<html lang="en">
<head>
<meta charset="utf-8">
<title>Still Ember — Price List</title>
<link rel="stylesheet" href="https://fonts.googleapis.com/css2?family=Noto+Serif:wght@400;600;700&display=swap">
<style>
  :root {
    --paper: #f1faea;
    --brown: #4a2312;
    --olive: #5d6f2e;
    --ink: #2f2a24;
    --navy: #33305a;
    --rule: #9aa872;
    --photo-warm: #e6dccb;
    --photo-cream: #f4efe6;
  }
  * { box-sizing: border-box; margin: 0; padding: 0; }
  html, body { width: 848px; height: 1200px; overflow: hidden; background: var(--paper); }
  body { font-family: "Noto Serif", Georgia, serif; color: var(--ink); }
  .sheet { position: relative; width: 848px; height: 1200px; background: var(--paper); overflow: hidden; }

  .photo { position: absolute; }
  .photo-cocoa { left: 0; top: 107px; width: 91px; height: 140px; border-radius: 0 40px 60px 0;
    background: radial-gradient(ellipse at 40% 45%, #a47a5c 0%, #c9ad94 45%, rgba(241,250,234,0) 75%); }
  .photo-lavender { left: 695px; top: 0; width: 122px; height: 126px;
    background: radial-gradient(ellipse at 50% 55%, #9d8fc8 0%, #c2badf 45%, rgba(241,250,234,0) 75%); }
  .photo-latte { left: 748px; top: 400px; width: 100px; height: 136px; border-radius: 68px 0 0 68px;
    background: radial-gradient(circle at 70% 50%, #c9a27a 0%, #e8d8c2 40%, #f5f2ea 62%, rgba(241,250,234,0) 80%); }
  .photo-candles { left: 141px; top: 731px; width: 272px; height: 231px; border-radius: 20px;
    background: radial-gradient(ellipse at 50% 55%, var(--photo-warm) 0%, var(--photo-cream) 50%, rgba(241,250,234,0) 80%); }

  .brand { position: absolute; left: 0; width: 848px; top: 62px; text-align: center;
    font-size: 50px; font-weight: 400; letter-spacing: 6px; color: var(--brown); line-height: 1; }
  .brand-dot { position: absolute; left: 416px; top: 130px; width: 14px; height: 14px; border-radius: 50%; background: var(--olive); }

  .title { position: absolute; left: 0; width: 848px; top: 187px; text-align: center;
    font-size: 36px; font-weight: 400; color: var(--brown); line-height: 1.1; }
  .title-rule { position: absolute; top: 208px; height: 1.5px; width: 60px; background: var(--olive); }
  .title-rule::before { content: ""; position: absolute; top: -2px; width: 5px; height: 5px; border-radius: 50%; background: var(--olive); }
  .title-rule.left { left: 260px; } .title-rule.left::before { left: -4px; }
  .title-rule.right { left: 528px; } .title-rule.right::before { right: -4px; }

  .range { position: absolute; }
  .range-mark { position: absolute; left: -20px; top: -34px; width: 1px; height: 70px;
    background: linear-gradient(var(--paper), var(--rule) 30%, var(--rule) 70%, var(--paper)); }
  .range-mark::before, .range-mark::after { content: ""; position: absolute; top: 33px; width: 5px; height: 5px;
    border-radius: 50%; background: var(--olive); }
  .range-mark::before { left: -9px; } .range-mark::after { left: 5px; }
  .range-name { font-size: 19px; font-weight: 600; color: var(--brown); line-height: 1; letter-spacing: 0.2px; white-space: nowrap; }
  .range-intro { margin-top: 16px; font-size: 13px; line-height: 15.4px; color: #2c2a28; }
  .price-list { margin-top: 16px; list-style: none; font-size: 13px; line-height: 15.4px; }
  .price-list li { white-space: nowrap; }
  .price-list b { font-weight: 600; }

  .closing { position: absolute; left: 0; width: 848px; text-align: center; font-size: 15.4px; line-height: 18.8px; color: var(--navy); }
  .order-box { position: absolute; left: 124px; top: 1083px; width: 600px; height: 85px;
    border: 1px dashed var(--rule); text-align: center; padding-top: 14px;
    font-size: 15.4px; line-height: 18.8px; color: var(--navy); }
  .order-email { color: var(--brown); }
</style>
</head>
<body>
<main class="sheet">
  <div class="photo photo-cocoa" role="img" aria-label="Chocolate curls and cocoa powder"></div>
  <div class="photo photo-lavender" role="img" aria-label="Sprig of lavender flowers"></div>
  <div class="photo photo-latte" role="img" aria-label="Cup of latte with leaf latte art"></div>
  <div class="photo photo-candles" role="img" aria-label="Two candles: a flower-topped lavender jar and a textured jar with a tag"></div>

  <h1 class="brand">STILL EMBER</h1>
  <span class="brand-dot"></span>

  <span class="title-rule left"></span>
  <h2 class="title">PRICE LIST</h2>
  <span class="title-rule right"></span>

  <section class="range" style="left:63px; top:290px; width:300px;">
    <span class="range-mark"></span>
    <h3 class="range-name">CORE LUXURY RANGE</h3>
    <p class="range-intro">Poured into beautiful, statement vessels, the Core Luxury Range features timeless jars designed to bring warmth, calm, and quiet luxury into your space.</p>
    <ul class="price-list"><li><b>Crystal Riviera – Luxury Jar – 400g</b> — $50</li></ul>
  </section>

  <section class="range" style="left:63px; top:457px; width:325px;">
    <span class="range-mark"></span>
    <h3 class="range-name">SIGNATURE INSPIRATION RANGE</h3>
    <p class="range-intro">These candles are more than scent — they are gentle reminders. Of your worth. Of your strength. Of the importance of choosing moments that nourish you. Created to support presence, self&#8209;connection, and intentional living.</p>
    <ul class="price-list">
      <li><b>Kingston Amber Jar – Bamboo Lid – 295g</b> — $30</li>
      <li><b>Opal Tiara Jar – 200g</b> — $40</li>
    </ul>
  </section>

  <section class="range" style="left:63px; top:659px; width:300px;">
    <span class="range-mark"></span>
    <h3 class="range-name">EVERYDAY ESSENTIALS</h3>
    <p class="range-intro">Simple, comforting candles designed for daily moments of calm and warmth.</p>
    <ul class="price-list"><li><b>Amber Jar – 150g</b> — $20</li></ul>
  </section>

  <section class="range" style="left:447px; top:290px; width:310px;">
    <span class="range-mark"></span>
    <h3 class="range-name">SUGAR ROW RANGE</h3>
    <p class="range-intro">A deliciously indulgent collection that looks almost good enough to eat and smells absolutely divine. The Sugar Row Collection fills your space with rich, comforting fragrance — a sweet sensory escape.</p>
    <ul class="price-list">
      <li><b>Strawberry Milkshake – 235g</b> — $35</li>
      <li><b>Chocolate Milkshake – 235g</b> — $35</li>
      <li><b>Caramel Popcorn – 295g</b> — $30</li>
      <li><b>Iced Coffee – 295g</b> — $30</li>
      <li><b>Café Latte – 295g</b> — $30</li>
    </ul>
  </section>

  <section class="range" style="left:447px; top:540px; width:330px;">
    <span class="range-mark"></span>
    <h3 class="range-name">BABY &amp; KEEPSAKE RANGE</h3>
    <p class="range-intro">Created to celebrate new life, this range is a soft welcome into the world. Gentle, meaningful candles designed to honour love, beginnings, and the light each little soul brings.</p>
    <ul class="price-list">
      <li><b>Hello, Little Light – Kingston Bowl Candle</b> — $55</li>
      <li><b>Hello, Little Light – Kingston Large Jar – 400g</b> — $40</li>
    </ul>
  </section>

  <section class="range" style="left:447px; top:729px; width:320px;">
    <span class="range-mark"></span>
    <h3 class="range-name">LIMITED EDITION RANGE</h3>
    <p class="range-intro">Small-batch candles released in limited numbers and available for a short time only.</p>
    <ul class="price-list" style="margin-top:26px;">
      <li><b>Soft Petals – 200g</b> — $30</li>
      <li><b>Ever Yours – Limited Edition – 400g</b> — $40</li>
      <li><b>Cuddle Cub Way – Kingston Bowl Candle</b> — $55</li>
    </ul>
  </section>

  <p class="closing" style="top:966px;">Still Ember is an evolving collection. New candle creations are introduced regularly,<br>and this price list may be updated to reflect new offerings and limited releases.</p>
  <p class="closing" style="top:1022px;">Each Still Ember candle is poured slowly and mindfully, with intention at its core —<br>because what we bring into our homes, and into our lives, truly matters.</p>

  <div class="order-box">
    Our website is currently being built. Online ordering will be available soon.<br>
    In the meantime, all orders can be placed by contacting us via email at<br>
    <span class="order-email">orders@stillember.com</span>.
  </div>
</main>
</body>
</html>
```